Swimming Pool Supply Company Business Cards

We need business cards designed for company. These need to be easy to edit so that we can fill in names, titles, and contact info for each person who works here.

Dalton R. Whitfield
Manager of Legal & Finance
K.L. Brisbane, Incorporated

4837 Grenway Avenue
Marlow Heights, PA 19243

E. dalton@klbrisbane-example.com
M. (215) 555-0173
O. (215) 555-0148

Contact Information for Business Card

Looking to upgrade current business cards with graphic that can be edited. Looking for fresh ideas for an age old industry.

Font styles to use
Serif
Sans Serif

Colors

Designer to choose colors to be used in the design.

Requirements
Must have
• Professional, fresh, unique but professional

```html
<!DOCTYPE html>
<html lang="en">
<head>
<meta charset="utf-8">
<title>Brisbane Business Cards</title>
<link rel="stylesheet" href="https://fonts.googleapis.com/css2?family=Montserrat:wght@400;500;600;700&display=swap">
<style>
  :root {
    --stage: #1c1c1c;
    --card-dark: #111111;
    --card-light: #ffffff;
    --ink: #1e1e1e;
    --ink-soft: #2f2f2f;
    --silver: #c9c9c9;
  }
  * { margin: 0; padding: 0; box-sizing: border-box; }
  html, body {
    width: 1200px;
    height: 900px;
    overflow: hidden;
    background: var(--stage);
    font-family: "Montserrat", Arial, sans-serif;
  }
  .sheet {
    position: relative;
    width: 1200px;
    height: 900px;
  }
  .card {
    position: absolute;
    left: 250px;
    width: 700px;
    height: 400px;
  }
  .card-back {
    top: 35px;
    background: var(--card-dark);
    display: flex;
    align-items: center;
    justify-content: center;
  }
  .card-back .wordmark {
    font-size: 72px;
    font-weight: 700;
    letter-spacing: 4px;
    color: var(--silver);
  }
  .card-front {
    top: 465px;
    background: var(--card-light);
    color: var(--ink);
  }
  .brand {
    position: absolute;
    top: 48px;
    right: 48px;
    text-align: right;
  }
  .brand .wordmark {
    font-size: 44px;
    font-weight: 700;
    letter-spacing: 2px;
    line-height: 1;
    color: var(--ink);
  }
  .brand .tagline {
    margin-top: 6px;
    font-size: 11.5px;
    font-weight: 500;
    color: var(--ink-soft);
  }
  .person {
    position: absolute;
    left: 60px;
    top: 120px;
  }
  .person .name {
    font-size: 25px;
    font-weight: 600;
    letter-spacing: 0.5px;
  }
  .person .title {
    margin-top: 2px;
    font-size: 16px;
    font-weight: 400;
    color: var(--ink-soft);
  }
  .contacts {
    list-style: none;
    margin-top: 16px;
  }
  .contacts li {
    display: flex;
    align-items: center;
    gap: 10px;
    font-size: 16px;
    line-height: 25px;
    color: var(--ink-soft);
  }
  .contacts svg {
    width: 12px;
    height: 12px;
    flex: none;
  }
  .address {
    position: absolute;
    left: 60px;
    top: 298px;
    font-style: normal;
    font-size: 16px;
    line-height: 24px;
    color: var(--ink-soft);
  }
</style>
</head>
<body>
<main class="sheet">
  <section class="card card-back" aria-label="Card back">
    <span class="wordmark">BRISBANE</span>
  </section>

  <section class="card card-front" aria-label="Card front">
    <div class="brand">
      <div class="wordmark">BRISBANE</div>
      <div class="tagline">Big Enough to Serve You, Small Enough to Care</div>
    </div>

    <div class="person">
      <div class="name">Dalton R. Whitfield</div>
      <div class="title">Manager of Legal &amp; Finance</div>
      <ul class="contacts">
        <li>
          <svg viewBox="0 0 12 12" aria-hidden="true"><rect x="3" y="0.5" width="6" height="11" rx="1" fill="none" stroke="#444" stroke-width="1.2"/><line x1="5" y1="9.5" x2="7" y2="9.5" stroke="#444" stroke-width="1"/></svg>
          (215) 555-0173
        </li>
        <li>
          <svg viewBox="0 0 12 12" aria-hidden="true"><path d="M3 1 L5 3.5 L4 5 Q5 7.5 7 8 L8.5 7 L11 9 L9.5 11 Q4 10.5 1 3 Z" fill="#444"/></svg>
          (215) 555-0148
        </li>
        <li>
          <svg viewBox="0 0 12 12" aria-hidden="true"><circle cx="6" cy="6" r="5" fill="none" stroke="#444" stroke-width="1.1"/><ellipse cx="6" cy="6" rx="2.2" ry="5" fill="none" stroke="#444" stroke-width="0.9"/><line x1="1" y1="6" x2="11" y2="6" stroke="#444" stroke-width="0.9"/></svg>
          www. Brisbane.Incorporated
        </li>
      </ul>
    </div>

    <address class="address">
      4837 Grenway Avenue<br>
      Marlow Heights, PA 19243
    </address>
  </section>
</main>
</body>
</html>
```